Harbour Thread Studio business card design

I need to get some business cards printed ready for company launch but my own designs look a bit basic and not very exciting, I hope you can help with something more eye catching.

I will be giving these to business owners, event organisers, brand managers etc. in a professional capacity with the aim that they keep me in mind and get in contact when they need to order embroidered/printed clothing items in future.
This is a basic website whilst new one is developed but the about us tab will give you better insight to the work i am looking for.

I also have facebook and instagram links on website so maybe if space for those icons?
also a business whatsapp account which there is a QR code for and something i may wish to include on the reverse so it's really easy for people to start a conversation.

Target Market(s)

Business to business

Industry/Entity Type

textile embroidery and printing

Contact Information for Business Card

name, job title, web address, email address

Font styles to use
Sans Serif
Other font styles liked:
• Monseratt is in the logo

Requirements
Must have
• name, job title, web address, email address, logo - nice design
Nice to have
• whatsapp qr link, social logos
Should not have
• no need for business address

```html
<!DOCTYPE html>
<html lang="en">
<head>
<meta charset="utf-8">
<title>Harbour Thread Studio – Business Card</title>
<link href="https://fonts.googleapis.com/css2?family=Open+Sans:wght@400;600;700&display=swap" rel="stylesheet">
<style>
  :root {
    --page-bg: #f1f4fb;
    --card-white: #ffffff;
    --brand-blue: #6a78ae;
    --brand-blue-light: #b8bdd9;
    --text-grey: #7b7b7b;
    --badge-ring: #7d7d7d;
    --shadow: 0 10px 28px rgba(60, 70, 110, 0.16);
  }
  * { box-sizing: border-box; margin: 0; padding: 0; }
  html, body {
    width: 972px; height: 1200px; overflow: hidden;
    background: var(--page-bg);
    font-family: "Open Sans", Arial, sans-serif;
  }
  .sheet { position: relative; width: 972px; height: 1200px; }

  .card {
    position: absolute; left: 106px; width: 760px; height: 434px;
    background: var(--card-white); box-shadow: var(--shadow); overflow: hidden;
  }
  .card--front { top: 126px; }
  .card--back  { top: 640px; }

  .card__art { position: absolute; inset: 0; width: 760px; height: 434px; }

  /* front */
  .brand-badge {
    position: absolute; left: 50px; top: 85px; width: 228px; height: 228px;
    border: 4px solid var(--badge-ring); border-radius: 50%;
    display: flex; align-items: center; justify-content: center; text-align: center;
  }
  .brand-name {
    color: var(--brand-blue); font-weight: 700; font-size: 27px;
    line-height: 1.2; text-transform: uppercase; letter-spacing: 1px;
  }
  .contact { position: absolute; left: 334px; top: 80px; }
  .contact__name {
    color: var(--brand-blue); font-weight: 700; font-size: 40px;
    letter-spacing: 0.3px; line-height: 1.1; text-transform: uppercase;
  }
  .contact__title { color: var(--text-grey); font-weight: 600; font-size: 22px; line-height: 1.2; margin-bottom: 18px; }
  .contact__list { list-style: none; }
  .contact__item {
    display: flex; align-items: center; gap: 8px;
    color: var(--text-grey); font-size: 21px; line-height: 27px;
  }
  .contact__icon { width: 14px; height: 14px; flex: none; }
  .contact__dot { width: 10px; height: 10px; border-radius: 50%; background: var(--text-grey); margin: 0 2px; flex: none; }
  .contact__web { color: var(--brand-blue); font-weight: 700; font-size: 22px; margin-top: 18px; }

  /* back */
  .back-badge {
    position: absolute; left: 259px; top: 97px; width: 240px; height: 240px;
    background: var(--card-white); border-radius: 50%;
    display: flex; align-items: center; justify-content: center; text-align: center;
  }
  .back-badge .brand-name { font-size: 28px; }
</style>
</head>
<body>
<main class="sheet">

  <section class="card card--front" aria-label="Business card front">
    <svg class="card__art" viewBox="0 0 760 434" aria-hidden="true">
      <path fill="var(--brand-blue)" d="M0 394 q9.5 -10 19 0 t19 0 t19 0 t19 0 t19 0 t19 0 t19 0 t19 0 t19 0 t19 0 t19 0 t19 0 t19 0 t19 0 t19 0 t19 0 t19 0 t19 0 t19 0 t19 0 t19 0 t19 0 t19 0 t19 0 t19 0 t19 0 t19 0 t19 0 t19 0 t19 0 t19 0 t19 0 t19 0 t19 0 t19 0 t19 0 t19 0 t19 0 t19 0 t19 0 V434 H0 Z"/>
    </svg>

    <div class="brand-badge">
      <p class="brand-name">Harbour<br>Thread<br>Studio</p>
    </div>

    <div class="contact">
      <h1 class="contact__name">Ewan Marlow</h1>
      <p class="contact__title">Director</p>
      <ul class="contact__list">
        <li class="contact__item">
          <svg class="contact__icon" viewBox="0 0 14 14" aria-hidden="true"><path fill="var(--text-grey)" d="M3 1 L5.5 1 L6 4.5 L4.5 5.5 Q5.5 8.5 8.5 9.5 L9.5 8 L13 8.5 L13 11 Q12 13 10 13 Q2 11 1 3 Q1 1 3 1 Z"/></svg>
          07700 900418
        </li>
        <li class="contact__item">
          <svg class="contact__icon" viewBox="0 0 14 14" aria-hidden="true"><rect x="0.5" y="2.5" width="13" height="9" fill="var(--text-grey)"/><path d="M1 3 L7 8 L13 3" fill="none" stroke="#fff" stroke-width="1.2"/></svg>
          ewan@harbourthreadstudio.com
        </li>
        <li class="contact__item">
          <span class="contact__dot" aria-hidden="true"></span>
          harbourthreadstudio
        </li>
      </ul>
      <p class="contact__web">harbourthreadstudio.com</p>
    </div>
  </section>

  <section class="card card--back" aria-label="Business card back">
    <svg class="card__art" viewBox="0 0 760 434">
      <rect width="760" height="434" fill="var(--brand-blue-light)" role="img" aria-label="Light blue band with a soft wave pattern"/>
      <path role="img" aria-label="Deep blue sea band with a soft wave pattern" fill="var(--brand-blue)" stroke="#ffffff" stroke-width="4" d="M-2 216 q9.5 -9 19 0 t19 0 t19 0 t19 0 t19 0 t19 0 t19 0 t19 0 t19 0 t19 0 t19 0 t19 0 t19 0 t19 0 t19 0 t19 0 t19 0 t19 0 t19 0 t19 0 t19 0 t19 0 t19 0 t19 0 t19 0 t19 0 t19 0 t19 0 t19 0 t19 0 t19 0 t19 0 t19 0 t19 0 t19 0 t19 0 t19 0 t19 0 t19 0 t19 0 t19 0 V440 H-2 Z"/>
    </svg>
    <div class="back-badge">
      <p class="brand-name">Harbour<br>Thread<br>Studio</p>
    </div>
  </section>

</main>
</body>
</html>
```